We need a web page design for a new company called "Quarry". We provide an innovative music sharing mobile application that allows music listeners to share their music without paying for a monthly subscription. We would like to incorporate the attached logo and color scheme. The final design should communicate music gifting and sharing.

Industry/Entity Type

It Company

```html
<!DOCTYPE html>
<html lang="en">
<head>
<meta charset="utf-8">
<title>Quarry — Music for everyone</title>
<link href="https://fonts.googleapis.com/css2?family=Roboto:wght@400;500;700&display=swap" rel="stylesheet">
<style>
  :root {
    --canvas-bg: #3f7f73;
    --brand-green: #5aa818;
    --brand-green-light: #79c23a;
    --brand-green-dark: #4a9410;
    --ink: #111111;
    --white: #ffffff;
    --footer-bg: #000000;
    --footer-link-green: #4f9a1a;
    --arrow-circle: rgba(150,150,150,0.85);
    --hero-tone-a: #2b2b2d;
    --hero-tone-b: #5a5a5e;
    --band-tone-a: #3a3327;
    --band-tone-b: #7b7060;
  }
  * { box-sizing: border-box; margin: 0; padding: 0; }
  html, body { width: 1200px; height: 900px; overflow: hidden; }
  body {
    background: var(--canvas-bg);
    font-family: "Roboto", Arial, sans-serif;
    position: relative;
  }
  .page {
    position: absolute; left: 351px; top: 22px;
    width: 518px; height: 833px;
    background: var(--white);
    box-shadow: 0 8px 30px rgba(0,0,0,0.35);
    overflow: hidden;
  }
  .abs { position: absolute; }

  /* Navigation */
  .nav {
    left: 0; top: 0; width: 518px; height: 28px;
    background: linear-gradient(to bottom, var(--brand-green-light), var(--brand-green-dark));
    color: var(--white);
  }
  .brand { display: flex; align-items: center; gap: 4px; font-weight: 500; color: var(--white); }
  .brand-dot { width: 11px; height: 11px; border-radius: 50%; background: var(--white); }
  .nav .brand { left: 37px; top: 6px; font-size: 13px; }
  .nav-link { top: 10px; font-size: 7px; }
  .nav-cta { right: 69px; top: 9px; font-size: 9px; font-weight: 700; }
  .nav-cta-icon { left: 461px; top: 5px; }

  /* Hero */
  .hero {
    left: 0; top: 28px; width: 518px; height: 231px;
    background: radial-gradient(ellipse at 55% 40%, var(--hero-tone-b), var(--hero-tone-a) 75%);
  }
  .hero-title {
    left: 0; width: 518px; top: 86px; text-align: center;
    color: var(--white); font-size: 22px; font-weight: 700; letter-spacing: -0.3px;
  }
  .hero-sub {
    left: 0; width: 518px; top: 111px; text-align: center;
    color: var(--white); font-size: 14px;
  }
  .hero-button {
    left: 214px; top: 141px; width: 88px; height: 17px;
    background: var(--brand-green); color: var(--white);
    font-size: 6.5px; font-weight: 500;
    display: flex; align-items: center; justify-content: center; gap: 5px;
  }
  .scroll-circle {
    width: 38px; height: 38px; border-radius: 50%;
    background: var(--arrow-circle);
    display: flex; align-items: center; justify-content: center;
  }

  /* Feature sections */
  .feature-heading { font-size: 18px; font-weight: 400; color: var(--ink); }
  .feature-body { font-size: 8.5px; line-height: 11px; color: var(--ink); width: 280px; }
  .section-intro { left: 0; top: 259px; width: 518px; height: 174px;
    background: linear-gradient(160deg, #ffffff 60%, #e6e6e6); }
  .brand-tile {
    left: 345px; top: 302px; width: 135px; height: 88px;
    background: var(--brand-green);
    display: flex; align-items: center; justify-content: center;
  }
  .brand-tile .brand { font-size: 25px; gap: 8px; }
  .brand-tile .brand-dot { width: 20px; height: 20px; }

  .band {
    left: 0; top: 433px; width: 518px; height: 173px;
    background: linear-gradient(100deg, var(--band-tone-a), var(--band-tone-b) 45%, #2a2620 85%);
  }
  .player {
    left: 59px; top: 518px; width: 126px; height: 13px;
    background: #e8e8e8;
  }
  .band .feature-heading, .band-text { color: var(--white); }
  .band-heading { right: 38px; top: 497px; color: var(--white); }
  .band-body { right: 38px; top: 527px; text-align: right; color: var(--white); width: 260px; }

  .section-share { left: 0; top: 606px; width: 518px; height: 173px;
    background: linear-gradient(160deg, #ffffff 45%, #bdbdbd); }

  /* Footer */
  .footer { left: 0; top: 779px; width: 518px; height: 54px; background: var(--footer-bg); }
  .footer-link { font-size: 6.5px; color: var(--white); }
  .footer-link.legal { color: var(--footer-link-green); }
  .footer .brand { right: 38px; top: 12px; font-size: 12px; font-weight: 400; }
  .footer .brand-dot { width: 10px; height: 10px; }
  .copyright { right: 38px; top: 33px; font-size: 5px; color: #cccccc; }
</style>
</head>
<body>
<main class="page">

  <header class="nav abs">
    <div class="brand abs"><span class="brand-dot"></span>Quarry</div>
    <span class="nav-link abs" style="left:120px">Features</span>
    <span class="nav-link abs" style="left:160px">Sharing</span>
    <span class="nav-link abs" style="left:202px">About</span>
    <span class="nav-cta abs">Download Quarry!</span>
    <svg class="nav-cta-icon abs" width="16" height="18" viewBox="0 0 16 18">
      <path d="M8 1 V11 M3.5 6.5 L8 11 L12.5 6.5" fill="none" stroke="#fff" stroke-width="2.4"/>
      <path d="M1 16.5 H15" stroke="#fff" stroke-width="2.4"/>
    </svg>
  </header>

  <section class="hero abs" role="img" aria-label="Blurred photo of people walking through a busy indoor hall"></section>
  <h1 class="hero-title abs">Music for everyone.</h1>
  <p class="hero-sub abs">Share your music for free!</p>
  <a class="hero-button abs">
    <svg width="8" height="8" viewBox="0 0 8 8"><path d="M4 0.5 V5 M2 3 L4 5 L6 3 M0.8 7.2 H7.2" fill="none" stroke="#fff" stroke-width="1.3"/></svg>
    Download Quarry!
  </a>
  <div class="scroll-circle abs" style="left:239px;top:186px">
    <svg width="20" height="20" viewBox="0 0 20 20"><path d="M10 2 V16 M3.5 9.5 L10 16 L16.5 9.5" fill="none" stroke="#333" stroke-width="3.4"/></svg>
  </div>

  <section class="section-intro abs"></section>
  <h2 class="feature-heading abs" style="left:37px;top:308px">Lorem ipsum dolor sit amet!</h2>
  <p class="feature-body abs" style="left:37px;top:333px">Lorem ipsum dolor sit amet, consectetur adipiscing elit, sed do eiusmod tempor incididunt ut labore et dolore magna aliqua. Ut enim ad minim veniam.</p>
  <div class="brand-tile abs"><div class="brand"><span class="brand-dot"></span>Quarry</div></div>

  <section class="band abs" role="img" aria-label="Blurred photo of a crowd in a warmly lit hall"></section>
  <div class="player abs">
    <svg width="126" height="13" viewBox="0 0 126 13">
      <g fill="#5aa818">
        <path d="M8 4 L5 6.5 L8 9 Z M11 4 L8 6.5 L11 9 Z"/>
        <path d="M20 4 L23 6.5 L20 9 Z"/><rect x="23.5" y="4" width="1.2" height="5"/>
        <path d="M34 4 L37 6.5 L34 9 Z M37 4 L40 6.5 L37 9 Z"/>
        <rect x="48" y="6" width="16" height="1.5"/>
        <rect x="101" y="4.5" width="4" height="4" rx="1"/>
        <path d="M112 5 H114 L116 3.5 V9.5 L114 8 H112 Z"/>
      </g>
      <rect x="64" y="6" width="28" height="1.5" fill="#bbb"/>
    </svg>
  </div>
  <h2 class="feature-heading band-heading abs">Lorem ipsum dolor sit amet!</h2>
  <p class="feature-body band-body abs">Lorem ipsum dolor sit amet, consectetur adipiscing elit, sed do eiusmod tempor incididunt ut labore et dolore magna aliqua. Ut enim ad minim veniam.</p>

  <section class="section-share abs"></section>
  <h2 class="feature-heading abs" style="left:37px;top:658px">Lorem ipsum dolor sit amet!</h2>
  <p class="feature-body abs" style="left:37px;top:683px">Lorem ipsum dolor sit amet, consectetur adipiscing elit, sed do eiusmod tempor incididunt ut labore et dolore magna aliqua. Ut enim ad minim veniam.</p>
  <svg class="abs" style="left:368px;top:667px" width="90" height="50" viewBox="0 0 90 50" aria-label="Sharing between phones">
    <g fill="none" stroke="#4f9a1a" stroke-width="1.6">
      <rect x="2" y="15" width="10" height="19" rx="1.5"/>
      <rect x="75" y="2" width="10" height="19" rx="1.5"/>
      <rect x="75" y="29" width="10" height="19" rx="1.5"/>
    </g>
    <g stroke="#4f9a1a" stroke-width="3.5">
      <line x1="31" y1="25" x2="57" y2="12"/>
      <line x1="31" y1="25" x2="57" y2="38"/>
    </g>
    <g fill="#4f9a1a">
      <circle cx="31" cy="25" r="7"/><circle cx="57" cy="12" r="7"/><circle cx="57" cy="38" r="7"/>
    </g>
  </svg>
  <div class="scroll-circle abs" style="left:239px;top:726px">
    <svg width="20" height="20" viewBox="0 0 20 20"><path d="M10 18 V4 M3.5 10.5 L10 4 L16.5 10.5" fill="none" stroke="#fff" stroke-width="3.4"/></svg>
  </div>

  <footer class="footer abs">
    <a class="footer-link abs" style="left:37px;top:13px">About</a>
    <a class="footer-link abs" style="left:64px;top:13px">News</a>
    <a class="footer-link abs" style="left:91px;top:13px">Press</a>
    <a class="footer-link legal abs" style="left:37px;top:27px">Legal</a>
    <a class="footer-link legal abs" style="left:64px;top:27px">Cookies</a>
    <a class="footer-link legal abs" style="left:105px;top:27px">Privacy</a>
    <div class="brand abs"><span class="brand-dot"></span>Quarry</div>
    <p class="copyright abs">(c) 2014 Quarry LLC</p>
  </footer>

</main>
</body>
</html>
```